New Graphic Design Project

Design a simple and clean PowerPoint slide templates for a Board meeting. The slides should have predominantly white backgrounds and use the brand graphic standards (attached). I'm also attached a PowerPoint master that I don't like, as it's too basic.
The company name is Harbor Lane Gauging.
It sells, calibrates, services and repairs industrial and commercial scales of all types. In particular, Truck scales, floor scales, counting scales and benchtop scales.
The website is harborlanegauging.example but this are the old colors, so ignore the logo and colors. We are launching a new logo and new look. Several variations of the logo are available.

```html
<!DOCTYPE html>
<html lang="en">
<head>
<meta charset="utf-8">
<title>Concept 03 – Board Meeting Slides</title>
<link href="https://fonts.googleapis.com/css2?family=Russo+One&family=Inter:ital,wght@0,400;0,500;0,600;0,700;1,600;1,700&display=swap" rel="stylesheet">
<style>
  :root {
    --orange: #f7740f;
    --orange-bright: #f9931f;
    --orange-deep: #ff6a0a;
    --navy: #1d2f5e;
    --ink: #4a4a4a;
    --white: #ffffff;
    --edge: #d6d6d6;
    --photo-dark: #7a3f10;
    --photo-mid: #c8731e;
    --display: "Russo One", sans-serif;
    --text: "Inter", sans-serif;
  }
  * { margin: 0; padding: 0; box-sizing: border-box; }
  html, body { width: 749px; height: 1200px; overflow: hidden; }
  body {
    position: relative;
    background: linear-gradient(180deg, var(--orange-bright) 0%, #fa8419 45%, var(--orange-deep) 100%);
    font-family: var(--text);
  }
  .concept-title {
    position: absolute; left: 100px; top: 50px;
    font-family: var(--display); font-size: 34px; color: var(--white); letter-spacing: 0.5px;
  }
  .fonts-note {
    position: absolute; left: 100px; top: 92px;
    font-size: 16px; font-weight: 500; color: var(--white); letter-spacing: -0.3px;
  }
  .slide {
    position: absolute; background: var(--white);
    box-shadow: 0 8px 14px rgba(120, 50, 0, 0.25);
    overflow: hidden;
  }
  .slide-cover { left: 101px; top: 125px; width: 543px; height: 305px; }
  .slide-closing { left: 101px; top: 798px; width: 543px; height: 305px; }
  .photo-area {
    position: absolute; left: 0; top: 0; height: 100%; width: 420px;
    background: linear-gradient(90deg, var(--photo-dark) 0%, var(--photo-mid) 45%, rgba(230,150,70,0.6) 75%, rgba(255,255,255,0) 100%);
  }
  .cover-edge { position: absolute; right: 0; top: 0; width: 8px; height: 100%; background: var(--edge); }
  .brand {
    display: flex; align-items: center; gap: 5px;
    font-family: var(--display); color: var(--navy); white-space: nowrap;
  }
  .brand-square { background: var(--orange); flex: none; }
  .cover-brand { position: absolute; right: 24px; top: 32px; font-size: 13px; }
  .cover-brand .brand-square { width: 12px; height: 12px; }
  .cover-heading {
    position: absolute; right: 24px; top: 124px; text-align: right;
    font-family: var(--display); color: var(--orange); font-size: 34px; line-height: 33px;
  }
  .cover-rule { position: absolute; right: 24px; top: 196px; width: 80px; height: 2px; background: var(--orange); }
  .cover-tagline {
    position: absolute; right: 24px; top: 204px; text-align: right;
    font-style: italic; font-weight: 700; color: var(--navy); font-size: 9.5px; line-height: 11px;
  }
  .cover-url {
    position: absolute; right: 26px; top: 274px;
    font-family: var(--display); color: var(--orange); font-size: 8px;
  }
  .slide-content { width: 261px; height: 147px; }
  .slide-content::before {
    content: ""; position: absolute; left: 0; top: 0; width: 4px; height: 100%; background: var(--edge);
  }
  .pos-a { left: 101px; top: 461px; }
  .pos-b { left: 383px; top: 461px; }
  .pos-c { left: 101px; top: 629px; }
  .pos-d { left: 383px; top: 629px; }
  .slide-title {
    position: absolute; left: 20px; top: 14px;
    font-family: var(--display); color: var(--orange); font-size: 9px;
  }
  .slide-title::after {
    content: ""; position: absolute; left: 0; top: 15px; width: 16px; height: 1px; background: var(--orange);
  }
  .slide-brand { position: absolute; right: 12px; top: 15px; font-size: 4.2px; gap: 2px; }
  .slide-brand .brand-square { width: 3.5px; height: 3.5px; }
  .slide-intro {
    position: absolute; left: 20px; right: 16px; top: 40px;
    font-size: 4.3px; line-height: 7px; font-weight: 500; color: var(--navy);
  }
  .columns { position: absolute; left: 20px; right: 28px; display: flex; gap: 11px; }
  .columns.low { top: 62px; }
  .columns.high { top: 40px; }
  .column { flex: 1; font-size: 4px; line-height: 7.4px; color: var(--ink); text-align: justify; }
  .column-heading { font-weight: 600; color: var(--orange); font-size: 4px; }
  .single-column {
    position: absolute; left: 20px; right: 16px; top: 40px;
    font-size: 4px; line-height: 7.4px; color: var(--ink);
  }
  .single-column p + p { margin-top: 7.4px; }
  .slide-footer {
    position: absolute; left: 20px; right: 12px; bottom: 8px;
    display: flex; align-items: center; gap: 5px;
    font-family: var(--display); color: var(--orange); font-size: 3.8px;
  }
  .footer-rule { flex: 1; height: 0.6px; background: var(--orange); }
</style>
</head>
<body>
  <h1 class="concept-title">Concept 03</h1>
  <p class="fonts-note">Fonts used: Tactic Sans &amp; Aileron</p>

  <section class="slide slide-cover">
    <div class="photo-area" role="img" aria-label="Photo of an orange-toned truck driving at speed with motion blur"></div>
    <div class="cover-edge"></div>
    <div class="brand cover-brand"><span class="brand-square"></span>Harbor Lane Gauging</div>
    <h2 class="cover-heading">BOARD<br>MEETING</h2>
    <div class="cover-rule"></div>
    <p class="cover-tagline">Driving Accuracy.<br>Delivering Confidence.</p>
    <p class="cover-url">HarborLaneGauging.example</p>
  </section>

  <section class="slide slide-content pos-a">
    <h3 class="slide-title">Two Column with Heading</h3>
    <div class="brand slide-brand"><span class="brand-square"></span>Harbor Lane Gauging</div>
    <p class="slide-intro">Quarterly results show steady growth across calibration and service lines, with truck scale repairs leading demand this period.</p>
    <div class="columns low">
      <div class="column"><p class="column-heading">Key service highlights this quarter</p>Field teams completed more calibrations than planned, and repair turnaround improved across all regions while customer renewals stayed strong and costs held close to budget.</div>
      <div class="column"><p class="column-heading">Key service highlights this quarter</p>Field teams completed more calibrations than planned, and repair turnaround improved across all regions while customer renewals stayed strong and costs held close to budget.</div>
    </div>
    <div class="slide-footer"><span>HarborLaneGauging.example</span><span class="footer-rule"></span><span>2</span></div>
  </section>

  <section class="slide slide-content pos-b">
    <h3 class="slide-title">Two Column</h3>
    <div class="brand slide-brand"><span class="brand-square"></span>Harbor Lane Gauging</div>
    <p class="slide-intro">Quarterly results show steady growth across calibration and service lines, with truck scale repairs leading demand this period.</p>
    <div class="columns low">
      <div class="column">Field teams completed more calibrations than planned, and repair turnaround improved across all regions while customer renewals stayed strong and costs held close to budget.</div>
      <div class="column">Field teams completed more calibrations than planned, and repair turnaround improved across all regions while customer renewals stayed strong and costs held close to budget.</div>
    </div>
    <div class="slide-footer"><span>HarborLaneGauging.example</span><span class="footer-rule"></span><span>3</span></div>
  </section>

  <section class="slide slide-content pos-c">
    <h3 class="slide-title">Two Column Plain</h3>
    <div class="brand slide-brand"><span class="brand-square"></span>Harbor Lane Gauging</div>
    <div class="columns high">
      <div class="column">Field teams completed more calibrations than planned, and repair turnaround improved across all regions while customer renewals stayed strong and costs held close to budget.</div>
      <div class="column">Field teams completed more calibrations than planned, and repair turnaround improved across all regions while customer renewals stayed strong and costs held close to budget.</div>
    </div>
    <div class="slide-footer"><span>HarborLaneGauging.example</span><span class="footer-rule"></span><span>4</span></div>
  </section>

  <section class="slide slide-content pos-d">
    <h3 class="slide-title">Column</h3>
    <div class="brand slide-brand"><span class="brand-square"></span>Harbor Lane Gauging</div>
    <div class="single-column">
      <p>Field teams completed more calibrations than planned, and repair turnaround improved across all regions while customer renewals stayed strong and costs held close to budget.</p>
      <p>Quarterly results show steady growth across calibration and service lines, with truck scale repairs leading demand this period.</p>
      <p>Next steps include new benchtop scale offerings, expanded floor scale service contracts and a review of technician training for the coming year.</p>
    </div>
    <div class="slide-footer"><span>HarborLaneGauging.example</span><span class="footer-rule"></span><span>5</span></div>
  </section>

  <section class="slide slide-closing">
    <div class="photo-area" role="img" aria-label="Photo of an orange-toned truck driving at speed with motion blur"></div>
  </section>
</body>
</html>
```